Redesign of Smart Watch Gift Voucher-SEE ATTACHED CURRENT DESIGN

I need to redesign my existing design using all same content and elements.

MY ENVISION: I invision more of a professional advertisement type of flyer/voucher. Imagine how Corvel.com would create a professionally looking flyer promoting the lumo or veno.

you can get many ideas about professional design by looking at some of corvels flyer designs :
https://www.findora-example.net/search?q=lumo+advertisment&mode=img&ref=a83kd02mzq7

stock photos are attached, you do not have to use them all, you can use some or none i am open to your designs using your own images if you want...just make sure the smartwatch looks black

DO NOT LEAVE ANY CONTENT OR ELEMENTS OUT ON MOCK UP PLEASE

SEE ATTACHED CURRENT DESIGN

I need to redesign my existing design using all same content and elements. DO NOT LEAVE ANY CONTENT OR ELEMENTS OUT ON MOCK UP PLEASE

Target Market(s)

B2B-you can get many ideas about professional design by looking at some of corvels flyer designs :

Industry/Entity Type

Marketing

Requirements
Must have
• I need to redesign my existing design using all same content and elements. DO NOT LEAVE ANY CONTENT OR ELEMENTS OUT ON MOCK UP PLEASE

Nice to have

Should not have

```html
<!DOCTYPE html>
<html lang="en">
<head>
<meta charset="utf-8">
<title>Smart Watch Reward Voucher</title>
<link href="https://fonts.googleapis.com/css2?family=Oswald:wght@300;400;500;600&family=Open+Sans:ital,wght@0,400;0,600;0,700;1,400&display=swap" rel="stylesheet">
<style>
  :root {
    --ink: #0e1014;
    --orange: #e8922a;
    --orange-deep: #b9661c;
    --white: #ffffff;
    --soft: #d9dbe0;
    --rule: #3a3d45;
  }
  * { margin: 0; padding: 0; box-sizing: border-box; }
  html, body { width: 928px; height: 1200px; overflow: hidden; background: var(--ink); }
  .voucher {
    position: relative; width: 928px; height: 1200px; overflow: hidden;
    background: linear-gradient(180deg, #121419 0%, #1b1e25 45%, #16181e 70%, #0e1014 100%);
    font-family: "Open Sans", Arial, sans-serif; color: var(--white);
  }
  .sun { position: absolute; left: 0; top: 0; z-index: 0; }
  .hero-photo {
    position: absolute; left: 440px; top: 360px; width: 488px; height: 680px;
    background: radial-gradient(ellipse at 55% 30%, #3a3e48 0%, #262a32 40%, rgba(22,24,30,0) 75%);
  }
  .watch-large {
    position: absolute; left: -20px; top: -40px; width: 356px; height: 430px; z-index: 1;
    background: radial-gradient(circle at 55% 45%, #2e323a 0%, #15171c 55%, #08090b 80%);
    border-radius: 0 0 50% 50% / 0 0 40% 40%;
  }
  .watch-small {
    position: absolute; left: 306px; top: 262px; width: 214px; height: 226px; z-index: 1;
    background: radial-gradient(circle at 45% 45%, #30343c 0%, #14161a 55%, #0a0b0d 75%);
    border-radius: 50%;
  }
  .headline {
    position: absolute; right: 34px; top: 84px; text-align: right; z-index: 2;
    font-family: "Oswald", Impact, sans-serif; text-transform: uppercase; line-height: 1;
  }
  .headline .lead { display: block; font-size: 55px; font-weight: 500; letter-spacing: -0.5px; }
  .headline .product { display: block; font-size: 70px; font-weight: 600; color: var(--orange); margin-top: 8px; letter-spacing: -0.5px; }
  .headline-rule { position: absolute; left: 742px; top: 272px; width: 150px; height: 3px; background: var(--orange); z-index: 2; }
  .tagline {
    position: absolute; right: 36px; top: 308px; text-align: right; z-index: 2;
    font-family: "Oswald", Arial, sans-serif; font-weight: 300; font-size: 22px; line-height: 36px;
  }
  .tagline em { font-style: normal; color: var(--orange); }
  .features { position: absolute; left: 70px; top: 584px; }
  .features h2, .details h2 {
    font-size: 15.5px; font-weight: 600; color: var(--orange); text-transform: uppercase; letter-spacing: 0.2px;
  }
  .features ul { list-style: none; margin: 27px 0 0 25px; }
  .features li { font-size: 13px; line-height: 30.3px; color: var(--soft); }
  .details { position: absolute; left: 349px; top: 588px; width: 497px; }
  .details .intro { font-size: 12.6px; line-height: 21.6px; font-weight: 600; text-align: justify; }
  .details .intro strong { color: var(--orange); font-weight: 600; font-size: 13.4px; }
  .details h2 { margin-top: 23px; }
  .details .body { margin: 20px 0 0 25px; font-size: 12px; line-height: 21.6px; color: var(--soft); text-align: justify; }
  .quote { margin: 24px 0 0 25px; font-size: 12.4px; font-style: italic; color: var(--soft); }
  .quote cite { display: block; font-style: normal; font-weight: 600; margin: 4px 0 0 12px; color: var(--white); }
  .footer-rule { position: absolute; left: 48px; top: 1034px; width: 832px; height: 1px; background: var(--rule); }
  .certificate { position: absolute; left: 70px; top: 1078px; font-size: 16px; font-weight: 600; line-height: 45px; }
  .certificate span { font-weight: 400; font-style: italic; font-size: 19px; color: var(--soft); }
  .redeem { position: absolute; left: 400px; width: 472px; top: 1078px; text-align: center; }
  .redeem .note { font-size: 12.5px; color: var(--soft); text-transform: uppercase; }
  .redeem .url { font-size: 16px; font-weight: 700; color: var(--orange); margin-top: 4px; }
  .redeem .terms { font-size: 12.5px; font-weight: 700; margin-top: 16px; }
</style>
</head>
<body>
<main class="voucher">
  <div class="hero-photo" role="img" aria-label="Dimly lit hand wearing a black smart watch showing an outdoor walk workout"></div>
  <svg class="sun" width="520" height="520" viewBox="0 0 520 520" aria-hidden="true">
    <circle cx="222" cy="232" r="280" fill="var(--orange-deep)"/>
    <circle cx="210" cy="222" r="280" fill="var(--orange)"/>
  </svg>
  <div class="watch-large" role="img" aria-label="Black round smart watch showing time 09:49"></div>
  <div class="watch-small" role="img" aria-label="Black round smart watch showing time 09:35 with activity rings"></div>

  <h1 class="headline">
    <span class="lead">Enjoy your brand new</span>
    <span class="product">Smart Watch</span>
  </h1>
  <div class="headline-rule"></div>
  <p class="tagline">Take control of your life with your<br>new <em>Smart Fitness Watch.</em></p>

  <section class="features">
    <h2>Features</h2>
    <ul>
      <li>Pedomoter</li>
      <li>Distance Tracker</li>
      <li>Calorie Counter</li>
      <li>Heart Rate Monitor</li>
      <li>Blood Pressure Monitor</li>
      <li>Stopwatch</li>
      <li>Sleep Monitoring</li>
      <li>Phone Locator</li>
      <li>Reminders Feature</li>
      <li>Remote Camera</li>
      <li>Alarm Clock</li>
      <li>Waterproof</li>
    </ul>
  </section>

  <section class="details">
    <p class="intro"><strong>Congratulations, you have been rewarded with a Brand New Smart Fitness Watch shipped right to your door.</strong> Just pay shipping and handling. Your new Smart Fitness Watch has these features: sport mode, pedomoter, distance, calorie, heart rate, blood pressure, stopwatch, sleep monitoring, phone locator, reminders, remote camera, an alarm clock and much more!</p>
    <h2>How can we do this?</h2>
    <p class="body">We have a couple retail partners that we team up with to "crowd purchase" huge shipping containers that hold 10's of thousands of electronic products at 80-90% off retail. We simply pass our savings on to you as we do not profit from our electronic products. You are basically able to "piggy back" on our partnerships and buying power to get an attractive electronic premium for a fraction of the retail cost.</p>
    <h2>What others say?</h2>
    <blockquote class="quote">"Are you sure this is not a Norvik Orbit Smartwatch in DISGUISE???? I love mine."
      <cite>-Derek M. Atlantic City, NJ</cite>
    </blockquote>
  </section>

  <div class="footer-rule"></div>
  <div class="certificate">
    <div>Certificate ID: <span>91772-89218</span></div>
    <div>Expires: <span>10/03/2020</span></div>
  </div>
  <div class="redeem">
    <p class="note">View all the details of this special offer and redeem online at</p>
    <p class="url">WWW.PERKSANDBONUSES.COM</p>
    <p class="terms">*Terms and Conditions apply see website for details</p>
  </div>
</main>
</body>
</html>
```